Home page redesign for an international job board

Need a modern design based on current structure of the page. I am happy with the current structure and layout/architecture, not entirely happy with how it looks. While I still want to keep most of the elements in place ( especially the search box) I would like to get another look and feel - more appealing to any audience related to online job search

Home page is: www.lucrubrisa.ro

Target Market(s)

job seeekers and employers

Industry/Entity Type

Architecture

Number of Pages Required

1 page

Font styles to use
Sans Serif

Colors
33a6d7

Requirements
Must have
• Stay with the same structure: Seach box, latest jobs, articles
Nice to have
• Key element: search for jobs - this needs to be very clear

```html
<!DOCTYPE html>
<html lang="en">
<head>
<meta charset="utf-8">
<title>LucruBrisa – Job Board Home</title>
<link rel="stylesheet" href="https://fonts.googleapis.com/css2?family=Oswald:wght@400;500&family=Roboto:ital,wght@0,400;0,500;0,700;1,400&display=swap">
<style>
:root{
  --red:#c1080f;
  --red-dark:#a5060c;
  --topbar:#efefef;
  --ink:#222;
  --muted:#555;
  --blue-title:#2a6aa8;
  --card-top:#8fb4ea;
  --card-bottom:#77a1e2;
  --btn-blue:#2f7ac4;
  --panel-grey:#e8e8e8;
  --black:#141414;
  --white:#fff;
}
*{box-sizing:border-box;margin:0;padding:0}
html,body{width:670px;height:1200px;overflow:hidden;background:var(--white)}
body{position:relative;font-family:'Roboto',Arial,sans-serif;color:var(--ink)}
.abs{position:absolute}

/* top bar */
.topbar{left:0;top:0;width:670px;height:32px;background:var(--topbar)}
.topbar-left{left:50px;top:13px;font-size:7px;color:#333}
.topbar-auth{left:418px;top:12px;font-size:7px;color:#333;letter-spacing:.2px}
.topbar-cta{left:493px;top:0;width:128px;height:30px;background:var(--red);color:var(--white);font-size:9px;display:flex;align-items:center;justify-content:center;border-radius:0 0 3px 3px}

/* header */
.brand{left:52px;top:50px;display:flex;align-items:center;gap:5px}
.brand-mark{width:30px;height:30px;border-radius:50%;background:var(--red)}
.brand-name{font-size:17px;font-weight:500;color:#333}
.nav{top:60px;font-size:7px;color:#222;letter-spacing:.2px}
.nav.active{color:var(--red)}

/* hero */
.hero{left:0;top:94px;width:670px;height:336px;background:linear-gradient(100deg,#e4ebf1 0%,#b9c9d6 45%,#6f7f8d 72%,#3b434b 100%)}
.hero-caption{left:50px;top:269px;width:274px;height:87px;background:rgba(44,96,146,.72)}
.hero-title{left:66px;top:283px;font-family:'Oswald',sans-serif;font-size:30px;color:var(--white);line-height:1}
.hero-sub{left:66px;top:317px;font-family:'Oswald',sans-serif;font-size:16px;color:var(--white);line-height:1}
.hero-arrow{top:332px;width:20px;height:20px;border-radius:50%;background:#111}

/* search panel */
.search-shadow{left:60px;top:478px;width:552px;height:22px;border-radius:50%;background:radial-gradient(ellipse at center,rgba(0,0,0,.28),rgba(0,0,0,0) 70%)}
.search-panel{left:50px;top:367px;width:572px;height:122px;background:var(--red);border-radius:3px}
.search-title{left:67px;top:380px;font-size:10px;font-weight:500;color:var(--white)}
.field{height:31px;background:var(--white);border-radius:2px;font-size:7px;color:#333;display:flex;align-items:center;padding-left:10px}
.field-select{justify-content:space-between;padding-right:10px}
.search-btn{left:430px;top:442px;width:84px;height:32px;background:linear-gradient(#2b2b2b,#050505);color:var(--white);font-size:10px;display:flex;align-items:center;justify-content:center;border-radius:2px}
.advanced{left:534px;top:453px;font-size:7px;color:var(--white)}

/* intro */
.intro-title{left:0;top:514px;width:670px;text-align:center;font-size:11px;font-weight:700;color:var(--red)}
.intro-text{left:95px;top:536px;width:480px;text-align:center;font-size:6.4px;line-height:12px;color:var(--muted)}

/* features */
.feature{top:577px;width:180px;height:100px;background:linear-gradient(var(--card-top),var(--card-bottom));box-shadow:0 2px 3px rgba(0,0,0,.2)}
.feature svg{position:absolute;left:22px;top:14px}
.feature-title{position:absolute;left:53px;top:14px;font-size:10px;color:var(--white)}
.feature-text{position:absolute;left:53px;top:29px;width:115px;font-size:6px;line-height:11.5px;color:var(--white)}
.feature-btn{position:absolute;top:71px;width:58px;height:17px;background:linear-gradient(#fff,#dedede);border-radius:2px;font-size:6px;color:#333;display:flex;align-items:center;justify-content:center}

/* about panel */
.about{left:50px;top:700px;width:572px;height:94px;background:var(--panel-grey);border:1px solid #d6d6d6}
.about-title{left:67px;top:720px;font-size:9px;font-weight:500;color:var(--blue-title)}
.about-text{left:67px;top:738px;width:530px;font-size:6.4px;line-height:12px;color:var(--muted)}

/* app articles */
.article-frame{top:809px;width:181px;height:113px;border:1px solid #e2e2e2;background:var(--white);padding:4px}
.article-photo{width:100%;height:100%}
.article-title{top:932px;font-size:10px;color:var(--blue-title)}
.article-text{top:951px;width:185px;font-size:6.2px;line-height:12px;color:#333}
.article-btn{top:982px;width:57px;height:17px;background:linear-gradient(#3d8bd6,#2566ad);border-radius:2px;color:var(--white);font-size:6.3px;font-weight:700;display:flex;align-items:center;justify-content:center;box-shadow:0 1px 2px rgba(0,0,0,.3)}

/* footer */
.footer{left:0;top:1027px;width:670px;height:123px;background:var(--red)}
.footer-head{top:1052px;font-size:8px;color:var(--white);letter-spacing:.2px}
.footer-links{left:54px;top:1071px;list-style:none;font-size:6.3px;color:var(--white);line-height:13.6px}
.footer-links li::before{content:"▸ ";font-size:5px}
.quote{left:170px;top:1072px;width:135px;font-size:6px;font-style:italic;line-height:9.2px;color:var(--white)}
.quote-by{left:170px;top:1123px;font-size:6px;color:var(--white)}
.contact{left:369px;top:1072px;font-size:6.3px;line-height:11.5px;color:var(--white)}
.follow-text{left:508px;top:1071px;font-size:7px;color:var(--white)}
.social{top:1090px;width:19px;height:19px;border-radius:50%;border:1px solid rgba(255,255,255,.85)}
.bottom{left:0;top:1150px;width:670px;height:50px;background:var(--black);color:var(--white);font-size:7px;display:flex;align-items:center;justify-content:center}
</style>
</head>
<body>

<div class="abs topbar"></div>
<div class="abs topbar-left">Search job &nbsp;|&nbsp; Apply for a new career</div>
<div class="abs topbar-auth">REGISTER &nbsp;|&nbsp; LOG IN</div>
<div class="abs topbar-cta">EMPLOYER &amp; POST JOB</div>

<div class="abs brand"><span class="brand-mark"></span><span class="brand-name">LucruBrisa</span></div>
<div class="abs nav active" style="left:281px">SEARCH JOB</div>
<div class="abs nav" style="left:339px">MY ACCOUNT</div>
<div class="abs nav" style="left:402px">CAREER COUNSELING</div>
<div class="abs nav" style="left:492px">CONTACT</div>
<div class="abs nav" style="left:541px">EMPLOYER &amp; POST JOB</div>

<div class="abs hero" role="img" aria-label="Businessman in a dark suit with folded arms in a bright, blurred office meeting room"></div>
<div class="abs hero-caption"></div>
<div class="abs hero-title">LUCRUBRISA</div>
<div class="abs hero-sub">Neque porro quisquam est qui dolorem</div>
<div class="abs hero-arrow" style="left:573px"><svg width="20" height="20" viewBox="0 0 20 20"><path d="M11.5 6 7.5 10l4 4" fill="none" stroke="#fff" stroke-width="1.8"/></svg></div>
<div class="abs hero-arrow" style="left:598px"><svg width="20" height="20" viewBox="0 0 20 20"><path d="M8.5 6l4 4-4 4" fill="none" stroke="#fff" stroke-width="1.8"/></svg></div>

<div class="abs search-shadow"></div>
<div class="abs search-panel"></div>
<div class="abs search-title">SEARCH JOB CREATES ACCOUNT</div>
<div class="abs field" style="left:66px;top:401px;width:176px">SEARCH JOB</div>
<div class="abs field" style="left:248px;top:401px;width:176px">EMAIL ID</div>
<div class="abs field" style="left:430px;top:401px;width:176px">LOCATION</div>
<div class="abs field" style="left:66px;top:442px;width:176px">CITY</div>
<div class="abs field field-select" style="left:248px;top:442px;width:176px">SELECT CATEGORY<svg width="8" height="5" viewBox="0 0 8 5"><path d="M0 0h8L4 5z" fill="#333"/></svg></div>
<div class="abs search-btn">SEARCH</div>
<div class="abs advanced">ADVANCE SEARCH</div>

<div class="abs intro-title">SEARCH JOB CREATES ACCOUNT APPLY JOB OF MOBILE</div>
<p class="abs intro-text">Lorem Ipsum has been the industry's standard dummy text ever since the 1500s, when an unknown printer took a galley of type and scrambled it to make a type specimen book. It has survived not only five centuries, but also the leap into electronic typesetting, remaining essentially unchanged</p>

<div class="abs feature" style="left:50px">
  <svg width="20" height="18" viewBox="0 0 20 18"><path d="M10 1 5 6h3v5h4V6h3z" fill="#fff"/><path d="M2 11v5h16v-5h-3v2H5v-2z" fill="#fff"/></svg>
  <div class="feature-title">Post cv</div>
  <div class="feature-text">Nullam ornare fermentum pharetra. Sed iaculis quam id uam volutpat a lorem amdiam Nullam</div>
  <div class="feature-btn" style="left:54px">READ MORE</div>
</div>
<div class="abs feature" style="left:245px">
  <svg width="20" height="18" viewBox="0 0 20 18"><path d="M18 1 12 7M12 3v4h4M2 17l6-6M8 15v-4H4" fill="none" stroke="#fff" stroke-width="2"/></svg>
  <div class="feature-title">Create alerts jobs</div>
  <div class="feature-text">Nullam ornare fermentum pharetra. Sed iaculis quam id uam volutpat a lorem amdiam Nullam</div>
  <div class="feature-btn" style="left:55px">READ MORE</div>
</div>
<div class="abs feature" style="left:441px">
  <svg width="20" height="18" viewBox="0 0 20 18"><rect x="1" y="2" width="18" height="14" rx="1" fill="none" stroke="#fff" stroke-width="1.6"/><path d="M4 6h2M8 6h8M4 9h2M8 9h8M4 12h2M8 12h8" stroke="#fff" stroke-width="1.4"/></svg>
  <div class="feature-title">Monitoring applications</div>
  <div class="feature-text">Nullam ornare fermentum pharetra. Sed iaculis quam id uam volutpat a lorem amdiam Nullam</div>
  <div class="feature-btn" style="left:55px">READ MORE</div>
</div>

<div class="abs about"></div>
<div class="abs about-title">NEQUE PORRO QUISQUAM EST QUI DOLOREM IPSUM QUIA DOLOR SIT AMET</div>
<p class="abs about-text">Lorem Ipsum has been the industry's standard dummy text ever since the 1500s, when an unknown printer took a galley of type and scrambled it to make a type specimen book. It has survived not only five centuries, but also the leap into electronic typesetting, remaining essentially unchanged Lorem Ipsum has been the industry's standard dummy text ever since the 1500s, when an unknown printer took a galley of type and scrambled it to make a type specimen book.</p>

<div class="abs article-frame" style="left:48px"><div class="article-photo" role="img" aria-label="Hand holding a smartphone showing app icons in front of a laptop keyboard" style="background:linear-gradient(135deg,#3a4a6a,#8a93a8 55%,#2a2f3a)"></div></div>
<div class="abs article-frame" style="left:243px"><div class="article-photo" role="img" aria-label="Hand holding a white smartphone with a mobile operating system logo on screen" style="background:linear-gradient(135deg,#3c4a3e,#c8d6b0 50%,#5a6a72)"></div></div>
<div class="abs article-frame" style="left:441px"><div class="article-photo" role="img" aria-label="Hand holding a smartphone showing a social network login screen" style="background:linear-gradient(135deg,#1a1a1e,#4a5a80 55%,#222)"></div></div>

<div class="abs article-title" style="left:48px">Jobs apps for Orbit Phone</div>
<div class="abs article-title" style="left:243px">Jobs apps for Nimbus OS</div>
<div class="abs article-title" style="left:441px">Jobs requirement FriendHub</div>
<p class="abs article-text" style="left:49px">Lorem Ipsum has been the industry's standard dummy text ever since the 1500s, when an unknown printer took a galley of</p>
<p class="abs article-text" style="left:243px">Lorem Ipsum has been the industry's standard dummy text ever since the 1500s, when an unknown printer took a galley</p>
<p class="abs article-text" style="left:445px">Lorem Ipsum has been the industry's standard dummy text ever since the 1500s, when an unknown printer took a galley</p>
<div class="abs article-btn" style="left:48px">READ MORE</div>
<div class="abs article-btn" style="left:244px">READ MORE</div>
<div class="abs article-btn" style="left:445px">READ MORE</div>

<div class="abs footer"></div>
<div class="abs footer-head" style="left:54px">LINKS</div>
<div class="abs footer-head" style="left:170px">CLIENT'S TESTIMONIALS</div>
<div class="abs footer-head" style="left:368px">GET IN TOUCH</div>
<div class="abs footer-head" style="left:509px">FOLLOW US</div>
<ul class="abs footer-links">
  <li>Who we are</li><li>How we work</li><li>Skills</li><li>SMB Clinics</li><li>Blog</li>
</ul>
<p class="abs quote">" Lorem Ipsum has been the industry's standard dummy text ever since the 1500s, when an unknown printer took a galley of type and scrambled it to make a type specimen book. It has survived not only five centuries. "</p>
<div class="abs quote-by">Client name, City</div>
<div class="abs contact">Address : 1450 Harbor Lane,<br>Eastfield, NJ<br><br>Phone : 201 555 0148<br><br>Email : info@lucrubrisa.ro</div>
<div class="abs follow-text">Connect with our social network</div>
<div class="abs social" style="left:511px"></div>
<div class="abs social" style="left:538px"></div>
<div class="abs social" style="left:566px"></div>

<div class="abs bottom">Copyright © 2015. All Rights Reserved</div>

</body>
</html>
```